business card for law firm that reflects the web site -www.MarenHolt.com. That is pleasant to read

We need a business card for a small law firm. Your company designed our logo - tree of life - which I can provide to the designers. The card should be on both sides. Use the coloring from the web site (www.MarenHolt.com) and logo (I have several formats). I am attaching the logo, but not sure what format to use.

First side name of firm: Law Office of M.K. Holt, P.A. 4816 West Sorrelwood, Suite 300, Phoenix, AZ 85019, Phone: 602.555.0143, Fax: 602.555.0187, web site: www.MarenHolt.com, email: MHolt@MarenHolt.com.
Maren K. Holt Bankruptcy and Foreclosure Attorney & Counselor.
Back side (perhaps vertical) the logo and then Notes with lines. At the bottom: Proud to help people and small businesses file for bankruptcy protection. We are a debt relief agency.
Updates

I have several versions of the logo. Will be happy to share whatever you need. Added Sunday, April 3, 2016

Target Market(s)

everyone

Industry/Entity Type

Legal

Contact Information for Business Card

I prefer something unique (rounded edges, design that adopts my web site - www.MarenHolt.com.

Font styles to use
Serif

Requirements
Must have
• First side name of firm: Law Office of M.K. Holt, P.A. 4816 West Sorrelwood, Suite 300, Phoenix, AZ 85019, Phone: 602.555.0143, Fax: 602.555.0187, web site: www.MarenHolt.com, email: MHolt@MarenHolt.com.
• Maren K. Holt Bankruptcy and Foreclosure Attorney & Counselor.
• Back side (perhaps vertical) the logo and then Notes with lines. At the bottom: Proud to help people and small businesses file for bankruptcy protection. We are a debt relief agency.
• Green and brown colors that reflect the web site: www.MarenHolt.com
Should not have
• Type so small that older people cannot read.

```html
<!DOCTYPE html>
<html lang="en">
<head>
<meta charset="utf-8">
<title>M.K. Holt Business Card</title>
<link rel="stylesheet" href="https://fonts.googleapis.com/css2?family=Crimson+Text:ital,wght@0,400;0,600;1,400&display=swap">
<style>
  :root {
    --canvas: #e9e7e3;
    --paper: #ffffff;
    --forest: #1f4a2c;
    --forest-deep: #173a22;
    --bark: #5b2c18;
    --bark-deep: #4a2312;
    --cream: #f3e9dc;
    --ink-brown: #6b2d1a;
    --rule: #2c5a39;
  }
  * { box-sizing: border-box; margin: 0; padding: 0; }
  html, body { width: 1200px; height: 873px; overflow: hidden; }
  body {
    background: var(--canvas);
    font-family: "Crimson Text", Georgia, serif;
    display: flex;
    align-items: center;
    justify-content: center;
    gap: 50px;
  }
  .card {
    position: relative;
    width: 525px;
    height: 300px;
    border-radius: 14px;
    overflow: hidden;
    box-shadow: 0 6px 18px rgba(0,0,0,0.18);
  }

  /* Back side: notes */
  .card--notes { background: var(--paper); }
  .notes-lines {
    position: absolute;
    left: 160px; right: 40px; top: 38px;
    display: flex; flex-direction: column; gap: 30px;
  }
  .notes-lines span { display: block; height: 1.5px; background: var(--rule); }
  .notes-band {
    position: absolute; left: 0; right: 0; bottom: 0; height: 92px;
    background: linear-gradient(180deg, var(--forest), var(--forest-deep));
    color: var(--cream);
    padding: 18px 28px 0 150px;
  }
  .notes-band p { font-size: 15px; line-height: 1.35; }
  .notes-band .agency { font-weight: 600; font-size: 18px; }
  .mark--small {
    position: absolute; left: 22px; top: 160px;
    display: flex; align-items: center; gap: 8px;
  }
  .mark--small .mark-disc {
    width: 62px; height: 62px; border-radius: 50%;
    background: var(--bark);
  }
  .mark--small .mark-name {
    color: var(--forest); font-size: 15px; font-weight: 600;
    position: absolute; left: 0; top: -24px; white-space: nowrap;
  }

  /* Front side: contact */
  .card--contact {
    background: radial-gradient(ellipse at 60% 40%, var(--bark), var(--bark-deep));
  }
  .mark--large {
    position: absolute; left: 26px; top: 18px;
    display: flex; align-items: center; gap: 12px;
  }
  .mark--large .mark-disc {
    width: 128px; height: 128px; border-radius: 50%;
    background: var(--forest);
  }
  .mark--large .mark-name {
    color: var(--cream); font-size: 20px; font-weight: 600;
    align-self: flex-start; margin-top: 14px;
  }
  .name-band {
    position: absolute; left: 150px; right: 0; top: 152px; height: 58px;
    background: var(--paper);
    padding: 4px 18px 0 24px;
    text-align: right;
  }
  .name-band h1 {
    font-weight: 400; font-size: 34px; line-height: 1; color: var(--ink-brown);
  }
  .name-band .title { font-size: 12.5px; color: var(--ink-brown); margin-top: 3px; }
  .contact {
    position: absolute; left: 174px; top: 220px;
    color: var(--cream); font-size: 11.5px; line-height: 1.3;
    list-style: none;
  }
</style>
</head>
<body>
  <section class="card card--notes" aria-label="Back of card with notes">
    <div class="notes-lines"><span></span><span></span><span></span><span></span><span></span></div>
    <div class="mark mark--small">
      <span class="mark-disc"></span>
      <span class="mark-name">M.K. Holt</span>
    </div>
    <div class="notes-band">
      <p>Proud to help people and small businesses file for bankruptcy protection.</p>
      <p class="agency">We are a debt relief agency.</p>
    </div>
  </section>

  <section class="card card--contact" aria-label="Front of card with contact details">
    <div class="mark mark--large">
      <span class="mark-disc"></span>
      <span class="mark-name">M.K. Holt</span>
    </div>
    <div class="name-band">
      <h1>Maren K. Holt</h1>
      <p class="title">Bankruptcy and Foreclosure Attorney &amp; Counselor.</p>
    </div>
    <ul class="contact">
      <li>Law Office of M.K. Holt, P.A.</li>
      <li>4816 West Sorrelwood, Suite 300, Phoenix, AZ 85019</li>
      <li>P 602.555.0143 | Fax 602.555.0187</li>
      <li>www.MarenHolt.com</li>
      <li>MHolt@MarenHolt.com</li>
    </ul>
  </section>
</body>
</html>
```